Business Card Design Project

We are a distribution company providing goods to Latin America. We sell everything from Medical equipment, generic medicines, to carecliners. The logo that we use is attached. The logo can incorporate different colors other than black for versatility. The company name is Valdoria International Corporation and/or VIC. The card will be printed using 1 or more of the following: Silk mounted and/or embossed. So if the design ideas could be made to incorporate that technique or any other unique techniques, it would be great. The target market is dialysis centers/doctors.

Basic Info for card:
Marnie Dowsett
Purchasing Manager
555-317-4086 direct
555-241-7953 fax
marnie.dowsett@valdoriavic.example
www.valdoriavic.example

Target Market(s)

Latin America

Industry/Entity Type

Business

Requirements
Nice to have
• The Front of the card should have the basic contact information with company name/logo. The back of the card could incorporate

```html
<!DOCTYPE html>
<html lang="en">
<head>
<meta charset="utf-8">
<title>Marnie Dowsett — Valdoria International Corporation</title>
<link rel="stylesheet" href="https://fonts.googleapis.com/css2?family=Alegreya+Sans+SC:wght@400;500&display=swap">
<style>
  :root {
    --paper-light: #eeeee0;
    --paper: #e8e9d5;
    --ink: #1f2926;
    --ink-soft: #2c3532;
    --brand-green: #346b0b;
  }
  html, body {
    margin: 0;
    padding: 0;
    overflow: hidden;
  }
  body {
    width: 1200px;
    height: 704px;
    background: var(--paper);
  }
  .card {
    position: relative;
    width: 1200px;
    height: 704px;
    overflow: hidden;
    background: radial-gradient(ellipse at 60% 30%, var(--paper-light) 0%, var(--paper) 75%);
    font-family: "Alegreya Sans SC", "Helvetica Neue", Arial, sans-serif;
    color: var(--ink);
  }
  .identity {
    position: absolute;
    left: 63px;
    top: 178px;
  }
  .identity__name {
    margin: 0;
    font-weight: 500;
    font-size: 56px;
    line-height: 1;
    letter-spacing: 1px;
  }
  .identity__role {
    margin: 6px 0 0 1px;
    font-weight: 400;
    font-size: 33px;
    line-height: 1;
    color: var(--ink-soft);
    letter-spacing: 0.5px;
  }
  .contact {
    position: absolute;
    left: 62px;
    top: 364px;
    margin: 0;
    padding: 0;
    list-style: none;
    font-size: 20px;
    line-height: 31px;
    color: var(--ink-soft);
    letter-spacing: 0.6px;
  }
  .contact__gap {
    margin-top: 30px;
  }
  .contact__label {
    display: inline-block;
    margin-right: 4px;
  }
  .brand {
    position: absolute;
    right: 62px;
    bottom: 58px;
    display: flex;
    align-items: center;
    gap: 14px;
    color: var(--brand-green);
    font-weight: 500;
    font-size: 64px;
    line-height: 1;
    letter-spacing: 4px;
  }
  .brand__dot {
    width: 26px;
    height: 26px;
    border-radius: 50%;
    background: var(--brand-green);
  }
</style>
</head>
<body>
  <main class="card">
    <header class="identity">
      <h1 class="identity__name">Marnie Dowsett</h1>
      <p class="identity__role">Purchasing Manager</p>
    </header>

    <ul class="contact">
      <li><span class="contact__label">TEL :</span> 555-317-4086</li>
      <li><span class="contact__label">FAX :</span> 555-241-7953</li>
      <li class="contact__gap">MARNIE.DOWSETT@VALDORIAVIC.EXAMPLE</li>
      <li>WWW.VALDORIAVIC.EXAMPLE</li>
    </ul>

    <div class="brand" aria-label="Valdoria International Corporation">
      <span class="brand__dot" aria-hidden="true"></span>
      <span class="brand__name">VIC</span>
    </div>
  </main>
</body>
</html>
```